Disability and mental health support work company requires business card

Specialising
Wrenfield Disability is a new QCAP service aimed toward QCAP participants with a history of criminal justice, psychosocial/mental health, intellectual, and cognitive disabilities.

Our focus
Focusing on providing core QCAP supports for community participation, daily activities and supported independent living.

Authentic
Likeminded people wanting to make a difference in participant's lives.

Our aim to provide holistic and empowering supports targeted towards creating independence and guidance for all participants and families.
Over 35 years of experience working with people that have psychosocial, intellectual, and cognitive disabilities.

Industry/Entity Type

disability and mental health

Contact Information for Business Card

logo - business name

Colors
0054AA
0677BA
7BADD7
CADEEF
E8F1F8
FFF300
FFF600
FEFA6F
FFFEC7
FFFEE8

Requirements
Must have
• want double sided business cards(wont let me change it)
Should not have
• any disability related pictures

```html
<!DOCTYPE html>
<html lang="en">
<head>
<meta charset="utf-8">
<title>Wrenfield Disability – Business Card</title>
<link rel="stylesheet" href="https://fonts.googleapis.com/css2?family=Poppins:ital,wght@0,300;0,400;0,600;1,300&display=swap">
<style>
  :root {
    --page-bg: #2c2c2c;
    --card-top: #143a66;
    --card-bottom: #0f2f55;
    --brand-deep: #0a2240;
    --gold: #d5aa2c;
    --sky: #7aaad8;
    --ink-light: #e4eaf2;
    --ink-soft: #b9c6d6;
  }
  * { box-sizing: border-box; margin: 0; padding: 0; }
  html, body { width: 1200px; height: 1138px; overflow: hidden; }
  body {
    background: var(--page-bg);
    font-family: "Poppins", sans-serif;
    position: relative;
  }
  .card {
    position: absolute;
    border-radius: 16px;
    background: linear-gradient(180deg, var(--card-top), var(--card-bottom));
  }
  .card--front { left: 274px; top: 186px; width: 622px; height: 376px; }
  .card--back  { left: 277px; top: 608px; width: 617px; height: 374px; }

  .front__name {
    position: absolute; left: 0; right: 0; top: 200px;
    text-align: center;
    font-weight: 600; font-size: 40px; letter-spacing: 3px;
    color: var(--brand-deep);
    text-transform: uppercase;
  }
  .front__web {
    position: absolute; left: 0; right: 0; top: 320px;
    text-align: center;
    font-weight: 300; font-size: 16px; letter-spacing: 6px;
    color: var(--ink-light);
  }
  .front__web .accent { color: var(--gold); }

  .brand-seal {
    position: absolute; left: 425px; top: 40px;
    width: 164px; height: 164px; border-radius: 50%;
    border: 2.5px solid var(--sky);
    display: flex; align-items: center; justify-content: center;
    text-align: center;
    font-weight: 600; font-size: 16px; line-height: 1.3; letter-spacing: 1px;
    color: var(--sky);
    text-transform: uppercase;
  }
  .person { position: absolute; left: 27px; top: 196px; }
  .person__name {
    font-weight: 600; font-size: 24px; letter-spacing: 0.3px;
    color: var(--ink-light); text-transform: uppercase; line-height: 1.2;
  }
  .person__role {
    font-weight: 300; font-style: italic; font-size: 16px;
    color: var(--gold); line-height: 1.4;
  }
  .divider { position: absolute; left: 0; top: 0; }
  .contact {
    position: absolute; left: 27px; top: 277px;
    list-style: none;
  }
  .contact__item {
    display: flex; align-items: center; gap: 13px;
    height: 25px;
    font-weight: 300; font-size: 16px; color: var(--ink-light);
  }
  .contact__icon { width: 18px; height: 14px; flex: none; }
  .address {
    position: absolute; right: 27px; top: 302px;
    text-align: right;
    font-weight: 300; font-size: 16px; line-height: 25px;
    color: var(--ink-light);
  }
</style>
</head>
<body>

<section class="card card--front">
  <p class="front__name">Wrenfield Disability</p>
  <p class="front__web">www.wrenfield<span class="accent">disability</span>.com</p>
</section>

<section class="card card--back">
  <div class="brand-seal">Wrenfield<br>Disability</div>

  <div class="person">
    <p class="person__name">Daniel Hart</p>
    <p class="person__role">Managing Director</p>
  </div>

  <svg class="divider" width="617" height="374" viewBox="0 0 617 374" aria-hidden="true">
    <path d="M27 267 H350 C372 267 385 286 410 286 H590" fill="none" stroke="var(--gold)" stroke-width="1.5"/>
  </svg>

  <ul class="contact">
    <li class="contact__item">
      <svg class="contact__icon" viewBox="0 0 18 14" aria-hidden="true">
        <path d="M1 5 C1 1 17 1 17 5 L14 5 L13 3 H5 L4 5 Z" fill="var(--sky)"/>
        <path d="M4 6 H14 L16 13 H2 Z" fill="var(--sky)"/>
        <circle cx="9" cy="9.5" r="2" fill="var(--card-bottom)"/>
      </svg>
      <span>020-0417-3381</span>
    </li>
    <li class="contact__item">
      <svg class="contact__icon" viewBox="0 0 18 14" aria-hidden="true">
        <rect x="1" y="2" width="16" height="11" fill="var(--sky)"/>
        <path d="M1 2 L9 8.5 L17 2" fill="none" stroke="var(--card-bottom)" stroke-width="1.4"/>
      </svg>
      <span>daniel@wrenfielddisability.com</span>
    </li>
    <li class="contact__item">
      <svg class="contact__icon" viewBox="0 0 18 14" aria-hidden="true">
        <circle cx="9" cy="7" r="6.3" fill="var(--sky)"/>
        <g fill="none" stroke="var(--card-bottom)" stroke-width="0.9">
          <ellipse cx="9" cy="7" rx="2.8" ry="6.3"/>
          <path d="M2.7 7 H15.3 M3.6 4 H14.4 M3.6 10 H14.4 M9 0.7 V13.3"/>
        </g>
      </svg>
      <span>www.wrenfielddisability.com</span>
    </li>
  </ul>

  <p class="address">58 Harbour Row, Millbrook,<br>Eastvale, US 204719</p>
</section>

</body>
</html>
```